Letterhead & logo design project

We need a letterhead for a new company called Brackenwold Ltd a firm of Chartered Accountants and Chartered Tax Advisers based in Ashcombe Vale, Hampshire
Updates
Please include the following:
Chartered Accountants and Chartered Tax Advisers
Industry/Entity Type
It Company
Requirements
Must have
- Must have director's name at the bottom of the letterhead. Must also contain some wording at the bottom of the page to be provided by the NPRFA at a later date

```html
<!DOCTYPE html>
<html lang="en">
<head>
<meta charset="utf-8">
<title>Brackenwold Ltd – Letterhead Set</title>
<link rel="stylesheet" href="https://fonts.googleapis.com/css2?family=Open+Sans:wght@400&family=Roboto+Condensed:wght@400&display=swap">
<style>
  :root {
    --backdrop: #7a8a7c;
    --paper-white: #ffffff;
    --paper-cream: #fbfce6;
    --ink: #1c1c1c;
    --brand-red: #b5090f;
    --brand-pink: #f4b8b0;
    --rule-blue: #b9cfe0;
    --margin-red: #f0a4a4;
    --edge: #c9ccc4;
  }
  * { margin: 0; padding: 0; box-sizing: border-box; }
  html, body { width: 1200px; height: 964px; overflow: hidden; }
  body {
    background: var(--backdrop);
    position: relative;
    font-family: "Open Sans", Arial, sans-serif;
    color: var(--ink);
  }
  h1 { font-weight: 400; }
  .sheet {
    position: absolute;
    overflow: hidden;
    border: 1px solid var(--edge);
  }

  /* Ruled writing pad */
  .pad {
    left: 12px; top: 41px; width: 586px; height: 899px;
    background-color: var(--paper-white);
    background-image: repeating-linear-gradient(
      to bottom,
      transparent 0, transparent 30px,
      var(--rule-blue) 30px, var(--rule-blue) 31px);
    background-position: 0 104px;
    background-size: 100% calc(100% - 104px);
    background-repeat: no-repeat;
  }
  .pad__header {
    position: absolute; left: 0; top: 0; width: 100%; height: 100px;
    background: var(--paper-white);
    border-bottom: 1px solid #9aa4ab;
    text-align: center;
  }
  .pad__flourish {
    position: absolute; left: 205px; top: 6px; width: 210px; height: 14px;
    background: linear-gradient(90deg, rgba(181,9,15,0), rgba(181,9,15,.55) 30%, rgba(181,9,15,.55) 70%, rgba(181,9,15,0));
    border-radius: 7px;
  }
  .pad__name {
    position: absolute; left: 40px; right: 0; top: 30px;
    font-size: 38px; line-height: 1; letter-spacing: -0.5px;
  }
  .pad__tagline {
    position: absolute; left: 40px; right: 0; top: 78px;
    font-family: "Roboto Condensed", "Arial Narrow", sans-serif;
    font-size: 10px; letter-spacing: -0.2px;
  }
  .pad__margin {
    position: absolute; top: 100px; bottom: 0; width: 1px;
    background: var(--margin-red);
  }
  .pad__margin--outer { left: 84px; }
  .pad__margin--inner { left: 93px; }

  /* Cream letterhead */
  .letter {
    left: 610px; top: 41px; width: 576px; height: 895px;
    background: var(--paper-cream);
  }
  .letter__shapes { position: absolute; inset: 0; }
  .letter__name {
    position: absolute; left: 0; width: 694px; top: 56px;
    text-align: center;
    font-size: 38px; line-height: 1; letter-spacing: -0.5px;
  }
  .letter__flourish {
    position: absolute; left: 196px; top: 112px; width: 300px; height: 18px;
    background: linear-gradient(90deg, rgba(181,9,15,0), rgba(181,9,15,.6) 25%, rgba(181,9,15,.6) 75%, rgba(181,9,15,0));
    border-radius: 9px;
  }
  .letter__tagline {
    position: absolute; left: 12px; top: 868px;
    font-family: "Roboto Condensed", "Arial Narrow", sans-serif;
    font-size: 9.5px; letter-spacing: -0.2px;
  }
</style>
</head>
<body>

  <section class="sheet pad">
    <div class="pad__margin pad__margin--outer"></div>
    <div class="pad__margin pad__margin--inner"></div>
    <header class="pad__header">
      <div class="pad__flourish" role="img" aria-label="Red calligraphic scroll flourish above the company name"></div>
      <h1 class="pad__name">Brackenwold Ltd</h1>
      <p class="pad__tagline">a firm of Chartered Accountants and Chartered Tax Advisers based in Ashcombe Vale, Hampshire</p>
    </header>
  </section>

  <section class="sheet letter">
    <svg class="letter__shapes" viewBox="0 0 576 895" width="576" height="895" aria-hidden="true">
      <path d="M0 0 H250 C165 38 68 112 0 170 Z" fill="var(--brand-pink)"/>
      <path d="M0 0 H234 C155 34 60 104 0 156 Z" fill="var(--brand-red)"/>
      <path d="M576 762 C500 822 430 868 330 895 H576 Z" fill="var(--brand-pink)"/>
      <path d="M576 774 C505 832 440 874 348 895 H576 Z" fill="var(--brand-red)"/>
    </svg>
    <h1 class="letter__name">Brackenwold Ltd</h1>
    <div class="letter__flourish" role="img" aria-label="Red calligraphic scroll flourish under the company name"></div>
    <p class="letter__tagline">a firm of Chartered Accountants and Chartered Tax Advisers based in Ashcombe Vale, Hampshire</p>
  </section>

</body>
</html>
```